Solo Law Practice Website Design

I am starting a solo law practice that will specialize in criminal defense and family law.

I have a rudimentary understanding of Wordpress as used through the tidalnest web services. The winning design would be compatible with this system so that I can modify content on my own.

I have supplied the written content and the components that I am looking for at the domain name: morganvaleslaw.com.

I would like to take that content and work it into a website that looks more professional and inviting. The two most important goals of the website are ease of navigation and rich content for search engine spiders (for example, integrating articles into pages rather than linking to a word document).

The winning design should be turnkey for me to upload immediately.
Updates

Reason: I will be traveling.

Target Market(s)

Individuals looking for legal services.

Industry/Entity Type

Defense

Requirements
Must have
• My picture should appear at least once in the site.

The design should allow a space for me to post blog or legal updates. Additionally, there should be functionality for me to add additional articles to the site.
Nice to have
• Appropriate pictures for a legal website to break-up text on pages.

Simple flash features that won't significantly slow loading times.

Widgets that drive traffic to a contact page or function.

```html
<!DOCTYPE html>
<html lang="en">
<head>
<meta charset="utf-8">
<title>Morgan Vales PLLC</title>
<link href="https://fonts.googleapis.com/css2?family=Didact+Gothic&family=Mulish:wght@700;800&display=swap" rel="stylesheet">
<style>
:root{
  --bg:#000;
  --orange:#ff8a00;
  --orange-deep:#e67c00;
  --text:#f2f2f2;
  --muted:#8a8a8a;
  --rule:#4a4a4a;
  --nav-border:#5a5a5a;
  --footer:#1b1b1b;
}
*{box-sizing:border-box;margin:0;padding:0}
html,body{width:847px;height:1200px;overflow:hidden;background:var(--bg)}
body{position:relative;font-family:"Didact Gothic",sans-serif;color:var(--text)}
.brand{position:absolute;left:15px;top:16px;font-family:"Mulish",sans-serif;font-weight:800;font-size:50px;letter-spacing:-0.5px;color:var(--text)}
.tagline{position:absolute;left:15px;top:82px;font-family:"Mulish",sans-serif;font-weight:700;font-size:15px;color:var(--muted)}
.main-nav{position:absolute;left:14px;top:116px;width:818px;height:48px;border:1px solid var(--nav-border);border-radius:8px;display:flex;overflow:hidden}
.main-nav a{flex:1;display:flex;align-items:center;justify-content:center;color:#fff;text-decoration:none;font-family:"Mulish",sans-serif;font-weight:700;font-size:13.5px;border-right:1px solid var(--nav-border)}
.main-nav a:last-child{border-right:none}
.main-nav a.active{background:var(--orange)}
.hero{position:absolute;left:14px;top:179px;width:818px;height:264px;border:1px solid #555;border-radius:8px;background:radial-gradient(ellipse at 45% 80%,#c8894a 0%,#7a3f18 35%,#3a1a0a 70%,#1a0b04 100%)}
.welcome{position:absolute;left:15px;top:464px;font-family:"Mulish",sans-serif;font-weight:800;font-size:25px;color:#777}
.welcome span{color:var(--text)}
.rule{position:absolute;left:15px;width:817px;height:1px;background:var(--rule)}
.portrait{position:absolute;left:15px;top:510px;width:192px;height:287px;background:linear-gradient(160deg,#3a2a1e 0%,#1c1410 55%,#0c0907 100%)}
.intro{position:absolute;left:223px;top:507px;width:609px;font-size:12px;line-height:18.2px}
.intro p{margin-bottom:18px}
.intro b{font-family:"Mulish",sans-serif;font-weight:800}
.areas-title{position:absolute;left:15px;top:844px;font-family:"Mulish",sans-serif;font-weight:700;font-size:14px;color:#777}
.area{position:absolute;top:878px;width:258px;height:222px}
.area h3{height:22px;background:var(--orange);color:#000;font-family:"Mulish",sans-serif;font-weight:800;font-size:14.5px;text-align:center;line-height:22px}
.area p{margin-top:9px;font-size:12px;line-height:18.2px;text-align:justify}
.area .more{position:absolute;right:0;top:206px;color:var(--orange);font-size:12px;text-decoration:none}
.divider{position:absolute;top:878px;width:1px;height:222px;background:var(--rule)}
.site-footer{position:absolute;left:14px;top:1136px;width:818px;height:50px;background:linear-gradient(#222,#141414);display:flex;align-items:center;justify-content:space-between;padding:0 48px 0 61px;font-size:12px}
.social{display:flex;align-items:center;gap:8px}
.social a{display:flex;align-items:center;gap:3px;color:#fff;text-decoration:none;font-size:11px}
.social i{width:10px;height:10px;background:#3a6fb8;border-radius:2px;display:inline-block}
</style>
</head>
<body>
<div class="brand">Morgan Vales PLLC</div>
<div class="tagline">Affordable Legal Representation</div>

<nav class="main-nav">
  <a class="active" href="#">Home</a>
  <a href="#">Criminal Law</a>
  <a href="#">Family Law</a>
  <a href="#">Fees</a>
  <a href="#">Legal Updates</a>
  <a href="#">Articles</a>
  <a href="#">Resources</a>
  <a href="#">Contact Us</a>
</nav>

<div class="hero" role="img" aria-label="Open law book on a desk with a laptop in front of shelves of leather-bound volumes"></div>

<h1 class="welcome">Welcome to <span>Morgan Vales PLLC</span></h1>
<div class="rule" style="top:500px"></div>

<div class="portrait" role="img" aria-label="Portrait of the attorney in a suit in front of bookshelves"></div>

<div class="intro">
  <p>Delivering legal services in the greater Twin Cities area.</p>
  <p><b>About Me.</b> My practice is focused on accomplishing your goals through results-oriented work at a discount price. For your convenience, I handle legal matters throughout the Twin Cities, including Hennepin, Ramsey, Anoka, and Washington counties. I understand that legal issues can appear complicated, and that is why I take a hands-on approach to guiding you through your legal needs.</p>
  <p><b>Personal Attention.</b> I control the size of my practice so that I am able to devote 100% of my effort to each case. I have no “associates” so I handle every case personally.</p>
  <p><b>General Practice.</b> I am available to provide your defense if you are accused of a felony or misdemeanor. Additionally, I can work with you on family matters such as divorce, child custody, wills, and nuptial agreements.</p>
  <p><b>In our first consultation,</b> I will take time to listen to your individual situation. I will explain the legal issues, and the risks involved in each course of action we may pursue so that you can make informed decisions about how to proceed.</p>
</div>

<h2 class="areas-title">My areas of specialization are as follows:</h2>
<div class="rule" style="top:868px"></div>

<section class="area" style="left:14px">
  <h3>Criminal Law</h3>
  <p>Convictions carry serious consequences and can often have a negative financial impact as well as putting your freedom in jeopardy. I know how to work on your behalf because I used to work at the Ramsey County Attorney’s Office and appeared on the prosecution’s behalf for more than 600 cases. I will prepare your defense, negotiate plea bargains if desired, or take the case to trial.</p>
  <a class="more" href="#">Read More .....</a>
</section>
<div class="divider" style="left:284px"></div>
<section class="area" style="left:294px">
  <h3>Experience Matters</h3>
  <p>Every case is different. You can take comfort knowing that I have appeared in court on a wide variety of cases including assault, drug possession and distribution, DWI, disorderly conduct, theft, burglary, domestic assault, check forgery, violations or orders for protection, firearms violations and DWI test refusals. I am also prepared to handle your probation violation or expungement.</p>
  <a class="more" href="#">Read More .....</a>
</section>
<div class="divider" style="left:563px"></div>
<section class="area" style="left:575px">
  <h3>Family Law</h3>
  <p>I am prepared to handle your family law concerns. I can guide you through the process of child custody matters, divorce, wills and nuptial agreements to ensure that you receive a fair and equitable result on these sensitive matters.</p>
  <a class="more" href="#">Read More .....</a>
</section>

<footer class="site-footer">
  <div class="social">Follow Us:
    <a href="#"><i></i>Circlebook</a>
    <a href="#"><i></i>Chirper</a>
    <a href="#"><i></i>Markly</a>
  </div>
  <div>© 2012 Law Offices of Morgan Vales PLLC</div>
</footer>
</body>
</html>
```